PLF Business Card Design

I am attaching my logo and want both a black and white modern, contemporary card for my business.

Below are the details I require on the cards and of course I would need to be able to change this.

Thanks

Rob

Robert K Ellison

Sales & Marketing Director

 

Vivid Panel Hub

PO Box 7319

Chatham

Kent

ME9 5QX

 

Tel +44 (0) 1579 618 203

Mobile: +44 (0) 7713 240 967

Fax: +44 (0) 1579 837 114

Email: rob@vividpanelhub.example

Website: www.vividpanelhub.example

 

 

Be part of a World full of imagination,

knowledge and inspiration

 

 

Derek Paxford

Editorial Director

 

Vivid Panel Hub

42 Harrow Gardens

Holmdon

Eastmarsh

TW6 8RN

 

Tel: +44 (0) 208 517 3926

Mobile: +44 (0) 7832 205 671

Email: derek@vividpanelhub.example

 

 

knowledge and inspiration

This is the same font as used in the logo.......

Robert K Ellison

 

Vivid Panel Hub

PO Box 7319

Chatham

Kent

ME9 5QX

 

Tel +44 (0) 1579 618 203

Fax: +44 (0) 1579 837 114

 

 

Derek Paxford

Editorial Director

 

Vivid Panel Hub

42 Harrow Gardens

Holmdon

Eastmarsh

TW6 8RN

 

Tel: +44 (0) 208 517 3926

Please add the following words to the back of the card and maybe add the logo to the back again.....

knowledge and inspiration

Robert K Ellison

 

Vivid Panel Hub

PO Box 7319

Chatham

Kent

ME9 5QX

 

Tel +44 (0) 1579 618 203

Fax: +44 (0) 1579 837 114

 

 

Derek Paxford

Editorial Director

 

Vivid Panel Hub

42 Harrow Gardens

Holmdon

Eastmarsh

TW6 8RN

 

Tel: +44 (0) 208 517 3926

knowledge and inspiration

Target Market(s)

Wide Format printing, Screen Printing, Digital Printing, Textile Printing, Signage, Digital Signage, Exhibition Graphics, Digital Textiles and more

Industry/Entity Type

Publishing

Requirements
Must have
• I would like to use these words on the back of the card both for a full black card and white card.

"Be part of a World full of imagination, knowledge and inspiration"

```html
<!DOCTYPE html>
<html lang="en">
<head>
<meta charset="utf-8">
<title>Vivid Panel Hub – Business Cards</title>
<link href="https://fonts.googleapis.com/css2?family=Rosario:wght@400;500;600&family=Arimo&display=swap" rel="stylesheet">
<style>
  :root {
    --board: #ffffff;
    --ink-black: #000000;
    --ink-white: #ffffff;
    --ink-grey: #6e6e6e;
    --accent: #f28c1e;
    --rule: #9a9a9a;
    --shadow: rgba(0,0,0,0.35);
  }
  * { margin: 0; padding: 0; box-sizing: border-box; }
  html, body { width: 1200px; height: 644px; overflow: hidden; background: var(--board); }
  body { position: relative; font-family: "Rosario", sans-serif; }

  .dimension-label { position: absolute; font-family: "Arimo", sans-serif; font-size: 22px; color: var(--ink-black); line-height: 1; }
  .dimension-label--width { left: 100px; top: 1px; }
  .dimension-label--height { left: 0; top: 71px; }
  .dimension-rule { position: absolute; background: var(--rule); }
  .dimension-rule--width { left: 101px; top: 26px; width: 451px; height: 1.5px; }
  .dimension-rule--height { left: 65.5px; top: 69px; width: 1.5px; height: 229px; }

  .card { position: absolute; width: 451px; height: 230px; box-shadow: 5px 6px 8px var(--shadow); }
  .card--dark { background: var(--ink-black); color: var(--ink-white); }
  .card--light { background: var(--ink-white); color: var(--ink-black); }
  .card--front-dark { left: 101.5px; top: 66px; }
  .card--front-light { left: 726px; top: 66px; }
  .card--back-dark { left: 101.5px; top: 390px; }
  .card--back-light { left: 726px; top: 390px; }

  .contact { position: absolute; left: 24px; top: 49px; }
  .contact__name { font-size: 16px; line-height: 18px; font-weight: 500; }
  .contact__role, .contact__email { font-size: 13px; line-height: 15px; }
  .card--light .contact__role, .card--light .contact__email, .card--light .contact__address { color: var(--ink-grey); }

  .divider { position: absolute; height: 9px; background: linear-gradient(to right, #8c8c8c, #d8d8d8 45%, #a8a8a8); }
  .card--light .divider { background: linear-gradient(to right, #8a8a8a, #cfcfcf 50%, #9d9d9d); }
  .divider--front { left: 22px; top: 111px; width: 180px; }
  .divider--back { left: 249px; top: 111px; width: 179px; }

  .contact__address { position: absolute; left: 24px; top: 129px; font-size: 13px; line-height: 15px; }
  .contact__phones { position: absolute; left: 24px; top: 162px; font-size: 13px; line-height: 15.5px; }
  .phone__key { display: inline-block; width: 16px; }
  .card--dark .phone__key { color: var(--accent); }

  .brand { position: absolute; left: 221px; top: 70px; display: flex; align-items: center; gap: 10px; }
  .brand__mark { width: 66px; height: 66px; border-radius: 50%; background: var(--accent); flex: none; }
  .brand__name { font-size: 19px; font-weight: 600; color: var(--accent); line-height: 1.1; width: 128px; }

  .tagline { position: absolute; right: 23px; text-align: right; color: var(--accent); font-size: 14.5px; letter-spacing: 1.6px; }
  .tagline--lead { top: 68px; line-height: 19px; }
  .tagline--close { top: 127px; line-height: 18.5px; }
  .website { position: absolute; left: 35px; top: 105px; font-size: 16.5px; line-height: 20px; }
  .card--light .website { color: var(--ink-grey); }
</style>
</head>
<body>
  <div class="dimension-label dimension-label--width">88mm</div>
  <div class="dimension-rule dimension-rule--width"></div>
  <div class="dimension-label dimension-label--height">45mm</div>
  <div class="dimension-rule dimension-rule--height"></div>

  <section class="card card--dark card--front-dark">
    <div class="contact">
      <p class="contact__name">Derek Paxford</p>
      <p class="contact__role">Managing Editor</p>
      <p class="contact__email">derek@vividpanelhub.example</p>
    </div>
    <div class="divider divider--front"></div>
    <p class="contact__address">42 Harrow Gardens, Holmdon,<br>Eastmarsh, TW6 8RN</p>
    <p class="contact__phones"><span class="phone__key">T</span>: +44 (0) 208 517 3926<br><span class="phone__key">M</span>: +44 (0) 7832 205 671</p>
    <div class="brand"><span class="brand__mark"></span><span class="brand__name">Vivid Panel Hub</span></div>
  </section>

  <section class="card card--light card--front-light">
    <div class="contact">
      <p class="contact__name">Derek Paxford</p>
      <p class="contact__role">Managing Editor</p>
      <p class="contact__email">derek@vividpanelhub.example</p>
    </div>
    <div class="divider divider--front"></div>
    <p class="contact__address">42 Harrow Gardens, Holmdon,<br>Eastmarsh, TW6 8RN</p>
    <p class="contact__phones"><span class="phone__key">T</span>: +44 (0) 208 517 3926<br><span class="phone__key">M</span>: +44 (0) 7832 205 671</p>
    <div class="brand"><span class="brand__mark"></span><span class="brand__name">Vivid Panel Hub</span></div>
  </section>

  <section class="card card--dark card--back-dark">
    <p class="tagline tagline--lead">Be part of<br>a World full of</p>
    <p class="website">www.vividpanelhub.example</p>
    <div class="divider divider--back"></div>
    <p class="tagline tagline--close">imagination<br>knowledge<br>and<br>inspiration</p>
  </section>

  <section class="card card--light card--back-light">
    <p class="tagline tagline--lead">Be part of<br>a World full of</p>
    <p class="website">www.vividpanelhub.example</p>
    <div class="divider divider--back"></div>
    <p class="tagline tagline--close">imagination<br>knowledge<br>and<br>inspiration</p>
  </section>
</body>
</html>
```